WordPress e-commerce new website design

Note: Completely changed the whole website design. Do not use red colors for the design.

We are seeking a talented website designer to create a WordPress e-commerce website for our business. The website will primarily focus on pre-purchase inspections for vehicles, with additional pages for parts, trucks/trailers, finance, and general information.

**Pages:**
1. Home
2. About
3. Pre-purchase Inspections
4. Parts
5. Trucks/Trailers
6. Finance

**Key Features:**
- Home page featuring a spot for a feature video
- Parts and trucks/trailers pages with multiple photos and videos for each item
- Pre-purchase inspections page with showcase video banners and sliders
- Cart functionality for parts
- Simple payment gateways for pre-purchase inspections, including Basic, Premium, and Extreme inspection levels, with corresponding prices
- Option for Fleet Inspection (3 or more vehicles) with a special quote request button
- Pop-up window on the home page prompting users to visit the pre-purchase inspections page
- Yellow payment buttons for easy visibility and user interaction

**Color Scheme:**
The designer can choose colors from blue, gold, yellow, black, white, and light gray.

**Requirements:**
- Proficiency in WordPress and e-commerce website design
- Experience with implementing payment gateways and cart functionality
- Ability to create visually appealing designs that align with our brand identity
- Strong attention to detail for creating new Design for semi-truck pre-purchase inspections website

```html
<!DOCTYPE html>
<html lang="en">
<head>
<meta charset="utf-8">
<title>Trukspec – Home</title>
<link href="https://fonts.googleapis.com/css2?family=Orbitron:wght@800;900&family=Lato:wght@400;700;900&display=swap" rel="stylesheet">
<style>
:root{
  --blue:#0a78e0;
  --blue-deep:#0556b8;
  --blue-light:#e6f2fc;
  --ink:#1b1b1b;
  --text:#555;
  --white:#fff;
  --gold:#ffd200;
  --price:#cf1f2a;
  --stage:#efefef;
  --night:#0c0f14;
}
*{margin:0;padding:0;box-sizing:border-box}
html,body{width:747px;height:1200px;overflow:hidden;background:var(--stage);font-family:'Lato',sans-serif}
.page{position:absolute;top:30.6px;width:662px;height:2305px;background:var(--white);transform:scale(0.494);transform-origin:0 0;overflow:hidden}
.page--home{left:26.2px}
.page--popup{left:393.2px}
.abs{position:absolute}
.head{font-family:'Orbitron',sans-serif;font-weight:900;letter-spacing:1px;color:var(--ink)}
.btn{position:absolute;display:flex;align-items:center;justify-content:center;border-radius:12px;font-size:9px;font-weight:700}
.btn--blue{background:linear-gradient(var(--blue),var(--blue-deep));color:var(--white)}
.btn--white{background:var(--white);color:var(--blue)}
.btn--gold{background:var(--gold);color:var(--blue-deep)}
.copy{font-size:7.6px;line-height:16.5px;color:var(--text)}
.nav{position:absolute;font-size:8.5px;color:var(--ink)}
.brand{position:absolute;font-weight:900;font-size:22px;letter-spacing:1px;color:var(--ink);display:flex;align-items:center;gap:6px}
.brand i{display:block;width:10px;height:10px;background:var(--blue);border-radius:50%}
.photo{position:absolute}
/* header */
.topbar{position:absolute;left:0;top:0;width:662px;height:82px;border-top:2px solid var(--blue)}
.icon-circle{position:absolute;width:20px;height:20px;border-radius:50%;background:var(--blue);display:flex;align-items:center;justify-content:center}
.call-label{position:absolute;font-size:5px;font-weight:700;color:var(--ink)}
.call-number{position:absolute;font-size:12px;color:var(--ink)}
/* hero */
.hero{position:absolute;left:0;top:82px;width:662px;height:343px;background:linear-gradient(135deg,#1c2430,#3a4250 45%,#232a34)}
.hero-title{position:absolute;left:0;width:662px;text-align:center;font-size:40px;color:var(--white)}
.hero-brand{color:var(--blue)}
.hero-text{position:absolute;left:120px;width:422px;top:256px;text-align:center;font-size:8.8px;line-height:17px;color:var(--white)}
/* pricing */
.card{position:absolute;background:var(--white);box-shadow:0 4px 14px rgba(0,0,0,.08);border-bottom:2px solid var(--blue);overflow:hidden;text-align:center}
.card-top{position:absolute;left:-20px;right:-20px;top:-40px;height:150px;border-radius:0 0 50% 50%;background:var(--blue-light)}
.card--featured .card-top{background:linear-gradient(160deg,var(--blue),var(--blue-deep))}
.card-name{position:absolute;left:0;right:0;font-size:7.5px;color:var(--blue)}
.card--featured .card-name,.card--featured .card-per{color:var(--white)}
.card-price{position:absolute;left:0;right:0;font-size:22px;font-weight:900;color:var(--price)}
.card-price sup{font-size:8px;vertical-align:top;margin-right:3px}
.card-per{position:absolute;left:0;right:0;font-size:6px;color:var(--blue)}
.card-list{position:absolute;left:0;right:0;font-size:5.8px;line-height:13.5px;color:var(--text)}
/* fleet */
.fleet-photo{position:absolute;left:0;top:1244px;width:662px;height:301px;background:linear-gradient(120deg,#2c3440,#5b6470 40%,#3b3a3a 70%,#1f2630)}
.fleet-band{position:absolute;left:0;top:1545px;width:662px;height:152px;background:linear-gradient(var(--blue),var(--blue-deep))}
.play{position:absolute;left:317px;top:1381px;width:28px;height:28px;border-radius:50%;background:var(--blue);display:flex;align-items:center;justify-content:center}
/* footer */
.footer{position:absolute;left:0;top:2100px;width:662px;height:205px}
.social{position:absolute;width:10px;height:10px;border-radius:2px;background:var(--blue)}
/* popup */
.overlay{position:absolute;inset:0;background:rgba(0,0,0,.8)}
.modal{position:absolute;left:64px;top:85px;width:560px;height:323px;background:linear-gradient(var(--blue),var(--blue-deep))}
</style>
</head>
<body>

<div class="page page--home">
  <header class="topbar">
    <div class="icon-circle" style="left:72px;top:17px"><svg width="10" height="10" viewBox="0 0 24 24"><path fill="#fff" d="M6.6 10.8a15 15 0 0 0 6.6 6.6l2.2-2.2c.3-.3.7-.4 1-.2 1.1.4 2.3.6 3.6.6.6 0 1 .4 1 1V20c0 .6-.4 1-1 1A17 17 0 0 1 3 4c0-.6.4-1 1-1h3.5c.6 0 1 .4 1 1 0 1.3.2 2.5.6 3.6.1.3 0 .7-.2 1z"/></svg></div>
    <div class="call-label" style="left:105px;top:17px">CALL US:</div>
    <div class="call-number" style="left:105px;top:25px">+1 555 010 2040</div>
    <div class="brand" style="left:268px;top:36px"><i></i>TRUKSPEC</div>
    <div class="btn btn--blue" style="left:498px;top:17px;width:66px;height:20px">Buy Parts</div>
    <div class="icon-circle" style="left:572px;top:17px"><svg width="10" height="10" viewBox="0 0 24 24"><path fill="#fff" d="M3 4h3l2.5 10h10l2-7H8" stroke="#fff" stroke-width="2" fill="none"/><circle cx="9" cy="19" r="2" fill="#fff"/><circle cx="17" cy="19" r="2" fill="#fff"/></svg></div>
    <div class="nav" style="left:74px;top:52px">Home</div>
    <div class="nav" style="left:122px;top:52px">About</div>
    <div class="nav" style="left:171px;top:52px">Trucks/Trailers</div>
    <div class="nav" style="left:442px;top:52px">Pre-purchase Inspections</div>
    <div class="nav" style="left:562px;top:52px">Finance</div>
  </header>

  <section class="hero" role="img" aria-label="Mechanics working under a lifted truck in a workshop">
    <div class="hero-title head" style="top:70px">WELCOME TO</div>
    <div class="hero-title head hero-brand" style="top:120px">TRUKSPEC</div>
    <p class="hero-text">On the other hand, we denounce with righteous indignation and dislike men who are so beguiled and demoralized by the charms of pleasure of the moment, so blinded by desire, that they cann</p>
    <div class="btn btn--white" style="left:226px;top:222px;width:99px;height:22px">Request A Quote</div>
    <div class="btn btn--blue" style="left:337px;top:222px;width:100px;height:22px">Join With Us</div>
  </section>
  <svg class="abs" style="left:0;top:355px" width="662" height="80" viewBox="0 0 662 80">
    <polygon fill="#0a78e0" points="0,9 125,7 331,55 537,7 662,7 662,80 0,80"/>
    <polygon fill="#fff" points="0,16 125,14 331,64 537,14 662,14 662,80 0,80"/>
  </svg>

  <section class="about">
    <h2 class="head abs" style="left:63px;top:510px;font-size:21px">ABOUT US</h2>
    <p class="copy abs" style="left:63px;top:543px;width:240px">On the other hand, we denounce with righteous indignation and dislike men who are so beguiled and demoralized by the charms of pleasure of the moment, so blinded by desire, that they cannot foresee the pain and trouble that are bound to ensue; and equal blame belongs to those who fail in their duty through weakness of will, which is the same as saying through shrinking from toil and pain.</p>
    <p class="copy abs" style="left:63px;top:659px;width:240px">These cases are perfectly simple and easy to distinguish. In a free hour, when our power of choice is untrammelled and when nothing prevents our being able to do what we like</p>
    <div class="btn btn--blue" style="left:63px;top:725px;width:62px;height:20px">Read More</div>
    <div class="photo" role="img" aria-label="Two mechanics reviewing a report beside an open engine bay" style="left:331px;top:490px;width:269px;height:278px;border-radius:8px;background:linear-gradient(135deg,#2b3b52,#4a5d78 50%,#1d2736)"></div>
  </section>

  <section class="pricing">
    <h2 class="head abs" style="left:0;width:662px;text-align:center;top:840px;font-size:19px">OUR PRICING</h2>
    <p class="abs" style="left:100px;width:462px;top:876px;text-align:center;font-size:8.6px;line-height:17px;color:var(--text)">On the other hand, we denounce with righteous indignation and dislike men who are so beguiled and demoralized by the charms of pleasure of the moment, so blinded by desire, that they cannot fore</p>

    <div class="card" style="left:90px;top:940px;width:158px;height:215px">
      <div class="card-top"></div>
      <div class="card-name" style="top:25px">BASIC&nbsp; INSPECTION</div>
      <div class="card-price" style="top:35px"><sup>$</sup>10.90</div>
      <div class="card-per" style="top:66px">Per Month</div>
      <div class="card-list" style="top:104px">Sed ut perspiciatis unde Omnis iste<br>Natus error sit volupt<br>Accusantium doloremque laudan Totam<br>Rperiam, eaque Ipsa quae ab illo<br>Unde Omnis iste natus error</div>
      <div class="btn btn--gold" style="left:42px;top:182px;width:75px;height:20px">Select Plan</div>
    </div>
    <div class="card" style="left:413px;top:940px;width:159px;height:215px">
      <div class="card-top"></div>
      <div class="card-name" style="top:25px">EXTREME INSPECTION</div>
      <div class="card-price" style="top:35px"><sup>$</sup>90.90</div>
      <div class="card-per" style="top:66px">Per Month</div>
      <div class="card-list" style="top:104px">Sed ut perspiciatis unde Omnis iste<br>Natus error sit volupt<br>Accusantium doloremque laudan Totam<br>Rperiam, eaque Ipsa quae ab illo<br>Unde Omnis iste natus error</div>
      <div class="btn btn--gold" style="left:42px;top:182px;width:75px;height:20px">Select Plan</div>
    </div>
    <div class="card card--featured" style="left:248px;top:928px;width:165px;height:240px;border-radius:4px 4px 0 0">
      <div class="card-top" style="top:-10px;height:100px;left:-14px;right:-14px"></div>
      <div class="card-name" style="top:37px">PREMIUM INSPECTION</div>
      <div class="card-price" style="top:47px"><sup>$</sup>50.90</div>
      <div class="card-per" style="top:78px">Per Month</div>
      <div class="card-list" style="top:116px">Sed ut perspiciatis unde Omnis iste<br>Natus error sit volupt<br>Accusantium doloremque laudan Totam<br>Rperiam, eaque Ipsa quae ab illo<br>Unde Omnis iste natus error</div>
      <div class="btn btn--gold" style="left:45px;top:194px;width:75px;height:20px">Select Plan</div>
    </div>
  </section>

  <section class="fleet">
    <div class="fleet-photo" role="img" aria-label="Feature video: mechanic greeting a couple in a tyre workshop"></div>
    <div class="play"><svg width="12" height="10" viewBox="0 0 12 10"><rect width="12" height="10" rx="2" fill="#fff"/><polygon points="4.5,2.5 8.5,5 4.5,7.5" fill="#0a78e0"/></svg></div>
    <div class="fleet-band">
      <h2 class="head abs" style="left:0;width:662px;text-align:center;top:26px;font-size:20px;color:#fff">REQUEST FOR FLEET INSPECTION</h2>
      <p class="abs" style="left:0;width:662px;text-align:center;top:66px;font-size:8.6px;color:#fff">On the other hand, we denounce with righteous indignation and dislike men who are so beguiled and</p>
      <div class="icon-circle" style="left:205px;top:101px;background:#fff"><svg width="10" height="10" viewBox="0 0 24 24"><path fill="#0a78e0" d="M6.6 10.8a15 15 0 0 0 6.6 6.6l2.2-2.2c.3-.3.7-.4 1-.2 1.1.4 2.3.6 3.6.6.6 0 1 .4 1 1V20c0 .6-.4 1-1 1A17 17 0 0 1 3 4c0-.6.4-1 1-1h3.5c.6 0 1 .4 1 1 0 1.3.2 2.5.6 3.6.1.3 0 .7-.2 1z"/></svg></div>
      <div class="call-label" style="left:235px;top:99px;color:#fff">CALL US:</div>
      <div class="call-number" style="left:234px;top:107px;color:#fff;font-size:13px">+1 555 010 2040</div>
      <div class="btn btn--white" style="left:363px;top:100px;width:95px;height:21px">Request A Quote</div>
    </div>
  </section>

  <section class="finance">
    <div class="photo" role="img" aria-label="Mechanic shaking hands with a client in a workshop" style="left:63px;top:1763px;width:268px;height:277px;border-radius:8px;background:linear-gradient(135deg,#3b4d66,#7a8696 50%,#2a3546)"></div>
    <h2 class="head abs" style="left:367px;top:1785px;font-size:19px">FINANCE</h2>
    <p class="copy abs" style="left:367px;top:1815px;width:240px">On the other hand, we denounce with righteous indignation and dislike men who are so beguiled and demoralized by the charms of pleasure of the moment, so blinded by desire, that they cannot foresee the pain and trouble that are bound to ensue; and equal blame belongs to those who fail in their duty through weakness of will, which is the same as saying through shrinking from toil and pain.</p>
    <p class="copy abs" style="left:367px;top:1931px;width:240px">These cases are perfectly simple and easy to distinguish. In a free hour, when our power of choice is untrammelled and when nothing prevents our being able to do what we like</p>
    <div class="btn btn--blue" style="left:367px;top:1998px;width:62px;height:20px">Read More</div>
  </section>

  <footer class="footer">
    <svg class="abs" style="left:0;top:0" width="662" height="205" viewBox="0 0 662 205">
      <polygon fill="#0a78e0" points="0,58 125,58 331,2 537,58 662,58 662,205 0,205"/>
      <polygon fill="#0c0f14" points="0,66 125,66 331,12 537,66 662,66 662,202 0,202"/>
    </svg>
    <div class="brand" style="left:258px;top:80px;color:#fff"><i></i>TRUKSPEC</div>
    <div class="nav" style="left:128px;top:129px;color:#fff">Home</div>
    <div class="nav" style="left:178px;top:129px;color:#fff">About Us</div>
    <div class="nav" style="left:242px;top:129px;color:#fff">Trucks/Trailers</div>
    <div class="nav" style="left:330px;top:129px;color:#fff">Parts</div>
    <div class="nav" style="left:377px;top:129px;color:#fff">Pre-purchase Inspections</div>
    <div class="nav" style="left:503px;top:129px;color:#fff">Finance</div>
    <div class="social" style="left:302px;top:153px"></div>
    <div class="social" style="left:317px;top:153px"></div>
    <div class="social" style="left:333px;top:153px"></div>
    <div class="social" style="left:349px;top:153px"></div>
    <div class="abs" style="left:0;width:662px;text-align:center;top:175px;font-size:6.5px;color:#fff">(C) Copyright 2024 | All Rights Reserved</div>
  </footer>
</div>

<div class="page page--popup">
  <header class="topbar">
    <div class="icon-circle" style="left:72px;top:17px"></div>
    <div class="call-label" style="left:105px;top:17px">CALL US:</div>
    <div class="call-number" style="left:105px;top:25px">+1 555 010 2040</div>
    <div class="brand" style="left:268px;top:36px"><i></i>TRUKSPEC</div>
    <div class="btn btn--blue" style="left:498px;top:17px;width:66px;height:20px">Buy Parts</div>
    <div class="icon-circle" style="left:572px;top:17px"></div>
    <div class="nav" style="left:74px;top:52px">Home</div>
    <div class="nav" style="left:122px;top:52px">About</div>
    <div class="nav" style="left:171px;top:52px">Trucks/Trailers</div>
    <div class="nav" style="left:442px;top:52px">Pre-purchase Inspections</div>
    <div class="nav" style="left:562px;top:52px">Finance</div>
  </header>
  <section class="hero" role="img" aria-label="Mechanics working under a lifted truck in a workshop"></section>
  <svg class="abs" style="left:0;top:355px" width="662" height="80" viewBox="0 0 662 80">
    <polygon fill="#0a78e0" points="0,9 125,7 331,55 537,7 662,7 662,80 0,80"/>
    <polygon fill="#fff" points="0,16 125,14 331,64 537,14 662,14 662,80 0,80"/>
  </svg>
  <h2 class="head abs" style="left:63px;top:510px;font-size:21px">ABOUT US</h2>
  <p class="copy abs" style="left:63px;top:543px;width:240px">On the other hand, we denounce with righteous indignation and dislike men who are so beguiled and demoralized by the charms of pleasure of the moment, so blinded by desire, that they cannot foresee the pain and trouble that are bound to ensue; and equal blame belongs to those who fail in their duty through weakness of will, which is the same as saying through shrinking from toil and pain.</p>
  <div class="btn btn--blue" style="left:63px;top:725px;width:62px;height:20px">Read More</div>
  <div class="photo" role="img" aria-label="Two mechanics reviewing a report beside an open engine bay" style="left:331px;top:490px;width:269px;height:278px;border-radius:8px;background:linear-gradient(135deg,#2b3b52,#4a5d78 50%,#1d2736)"></div>
  <h2 class="head abs" style="left:0;width:662px;text-align:center;top:840px;font-size:19px">OUR PRICING</h2>
  <div class="card" style="left:90px;top:940px;width:158px;height:215px"><div class="card-top"></div><div class="card-price" style="top:35px"><sup>$</sup>10.90</div><div class="btn btn--gold" style="left:42px;top:182px;width:75px;height:20px">Select Plan</div></div>
  <div class="card" style="left:413px;top:940px;width:159px;height:215px"><div class="card-top"></div><div class="card-price" style="top:35px"><sup>$</sup>90.90</div><div class="btn btn--gold" style="left:42px;top:182px;width:75px;height:20px">Select Plan</div></div>
  <div class="card card--featured" style="left:248px;top:928px;width:165px;height:240px"><div class="card-top" style="top:-10px;height:100px;left:-14px;right:-14px"></div><div class="card-price" style="top:47px"><sup>$</sup>50.90</div><div class="btn btn--gold" style="left:45px;top:194px;width:75px;height:20px">Select Plan</div></div>
  <div class="fleet-photo" role="img" aria-label="Feature video: mechanic greeting a couple in a tyre workshop"></div>
  <div class="fleet-band"><h2 class="head abs" style="left:0;width:662px;text-align:center;top:26px;font-size:20px;color:#fff">REQUEST FOR FLEET INSPECTION</h2></div>
  <div class="photo" role="img" aria-label="Mechanic shaking hands with a client in a workshop" style="left:63px;top:1763px;width:268px;height:277px;border-radius:8px;background:linear-gradient(135deg,#3b4d66,#7a8696 50%,#2a3546)"></div>
  <h2 class="head abs" style="left:367px;top:1785px;font-size:19px">FINANCE</h2>
  <footer class="footer">
    <svg class="abs" style="left:0;top:0" width="662" height="205" viewBox="0 0 662 205">
      <polygon fill="#0a78e0" points="0,58 125,58 331,2 537,58 662,58 662,205 0,205"/>
      <polygon fill="#0c0f14" points="0,66 125,66 331,12 537,66 662,66 662,202 0,202"/>
    </svg>
    <div class="brand" style="left:258px;top:80px;color:#fff"><i></i>TRUKSPEC</div>
  </footer>

  <div class="overlay"></div>
  <div class="modal" role="dialog" aria-label="Pre-purchase inspections">
    <div class="photo" role="img" aria-label="Salesman with a clipboard talking to a smiling couple in a showroom" style="left:24px;top:23px;width:248px;height:277px;background:linear-gradient(135deg,#dfe6ee,#8d9cb0 55%,#3d4c63)"></div>
    <h2 class="head abs" style="left:303px;top:72px;font-size:20px;line-height:32px;color:#fff">PRE-PURCHASE<br>INSPECTIONS</h2>
    <p class="abs" style="left:303px;top:141px;width:235px;font-size:7.4px;line-height:16.5px;color:#fff">On the other hand, we denounce with righteous indignation and dislike men who are so beguiled and demoralized by the charms of pleasure of the moment, so blinded by desire, that they cannot foresee the pain and trouble that are</p>
    <div class="btn btn--white" style="left:303px;top:226px;width:62px;height:20px">Click Here</div>
    <svg class="abs" style="left:533px;top:19px" width="11" height="11" viewBox="0 0 11 11"><circle cx="5.5" cy="5.5" r="5.5" fill="#fff"/><path d="M3.5 3.5l4 4M7.5 3.5l-4 4" stroke="#0a78e0" stroke-width="1.3"/></svg>
  </div>
</div>

</body>
</html>
```